Australian based company requires brochure design for new safety product.

New company with no Logo or branding - Let your imagination run wild.

Brontavel Pty Ltd need a brochure designed for marketing a safety product.
The idea of the brochure is to leave with Procurement departments of the health and safety industry for quick easy reference of product specifications and benefits.

Target Market(s)

Procurement teams of Health and Safety Industry. Quick easy reference points of specifications and benefits of product.

Industry/Entity Type

Marketing

Requirements
Must have
• Must have product details and specifications as per below, preferred format A4 sheet, front to back, with attached 6 photos, as well JPEG drawing attached.

With Government legislation a requirement all electrical cords be elevated a minimum of 2 meters on construction sites - THE CORVIMAX STAND was developed.
With over thirty years experience in the construction industry and safety requirements that continue to evolve we have designed and developed a lead stand that is ergonomic, portable and versatile. With no other product like it on the market.

BENEFITS
- Unique portable and easy to assemble Corvistand to fit in most tool boxes
- Non-conductive and highly visible
- Indoor and outdoor use
- Leads the way in working safely
- Complies with Government legislation
- Construction sites, Outdoor events and Camping grounds

FUNCTIONS
- Fully adjustable Telescopic Corvistand from 1.2 meters to 4.2 meters
- Spring loaded to lock between two surfaces
- Supports multiple leads, including temporary lighting and can also be used for Laser levels
- Can be screwed to a wall to elevate above floor finishes

For all enquires please contact brontavel@mailfern.example or Marisa Thorne 0491736628

```html
<!DOCTYPE html>
<html lang="en">
<head>
<meta charset="utf-8">
<title>Corvimax Stand Brochure</title>
<link href="https://fonts.googleapis.com/css2?family=Roboto:wght@700;900&family=Roboto+Condensed:wght@400;700&display=swap" rel="stylesheet">
<style>
  :root {
    --bg: #e9e6e1;
    --ink: #111111;
    --black: #141414;
    --white: #ffffff;
    --green: #7cc242;
    --sky-top: #eef2f5;
    --sky-low: #b9c9d6;
    --drawing-grey: #d9dde0;
  }
  * { margin: 0; padding: 0; box-sizing: border-box; }
  html, body { width: 1200px; height: 849px; overflow: hidden; background: var(--bg); }
  body { position: relative; font-family: "Roboto Condensed", Arial, sans-serif; }

  .page {
    position: absolute; top: 28px; width: 560px; height: 793px;
    background: var(--black); overflow: hidden;
    box-shadow: 0 4px 14px rgba(0,0,0,.25);
  }
  .page--front { left: 30px; }
  .page--back { left: 610px; }

  /* front */
  .front-hero {
    position: absolute; left: 0; top: 0; width: 560px; height: 380px;
    background: linear-gradient(180deg, var(--sky-top) 0%, #dfe6ec 45%, var(--sky-low) 100%);
  }
  .front-accent { position: absolute; left: 0; top: 200px; }
  .product-title {
    position: absolute; left: 24px; top: 150px; width: 400px;
    font-family: "Roboto Condensed", Arial, sans-serif; font-weight: 700;
    font-size: 54px; line-height: 1; color: var(--ink);
  }

  .photo-strip {
    position: absolute; left: 24px; top: 255px; width: 512px; height: 222px;
    border: 5px solid var(--white); border-radius: 22px; overflow: hidden;
    display: flex; gap: 5px; background: var(--white);
  }
  .photo { flex: 1; }
  .photo--rooftop { background: linear-gradient(180deg, #c9d8e6, #8d9aa6 70%, #6f7880); }
  .photo--city { background: linear-gradient(180deg, #cfdbe7, #7f8d99 60%, #9b9f9f); }
  .photo--worker { background: linear-gradient(180deg, #b7bfc4, #8f979b 50%, #d36a2b 75%, #5b6166); }

  .intro {
    position: absolute; left: 50px; top: 515px; width: 460px;
    color: var(--white); font-size: 18px; line-height: 1.3; text-align: center;
  }
  .intro strong { font-weight: 700; }

  /* back */
  .back-top {
    position: absolute; left: 0; top: 0; width: 560px; height: 300px;
    background: linear-gradient(180deg, #ffffff 0%, #f1f3f5 55%, #c8d2da 100%);
  }
  .back-accent { position: absolute; left: 0; top: 230px; }
  .section-title {
    font-family: "Roboto", Arial, sans-serif; font-weight: 900; font-size: 26px; letter-spacing: .5px;
  }
  .benefits { position: absolute; left: 12px; top: 14px; width: 212px; color: var(--ink); }
  .functions { position: absolute; left: 12px; top: 355px; width: 212px; color: var(--white); }
  .bullets { list-style: none; margin-top: 4px; }
  .bullets li { position: relative; padding-left: 10px; font-size: 13.5px; line-height: 1.22; margin-bottom: 2px; }
  .bullets li::before { content: "•"; position: absolute; left: 0; }

  .product-card {
    position: absolute; left: 12px; top: 252px; width: 210px; height: 72px;
    background: var(--white); border: 1px solid #cfd5da;
    display: flex; flex-direction: column; justify-content: space-between; padding: 6px 8px;
  }
  .product-card__name {
    font-family: "Roboto Condensed", Arial, sans-serif; font-weight: 700; color: var(--ink);
    font-size: 15px;
  }
  .product-card__drawing { height: 34px; background: var(--drawing-grey); }

  .side-photos {
    position: absolute; left: 236px; top: 18px; width: 190px; height: 520px;
    border: 4px solid var(--white); border-radius: 16px; overflow: hidden;
    background: var(--white); display: grid; grid-template-rows: 300px 1fr; gap: 4px;
  }
  .side-photos__lower { display: grid; grid-template-columns: 1fr 1fr; gap: 4px; }
  .photo--site-walk { background: linear-gradient(180deg, #9fb0bd, #7d847c 55%, #bdb7a9); }
  .photo--floor { background: linear-gradient(180deg, #c4c8c4, #6e6a60); }
  .photo--wall { background: linear-gradient(180deg, #e4e4e2, #b9bbbc); }

  .contact {
    position: absolute; left: 0; top: 590px; width: 440px; text-align: center; color: var(--white);
    font-family: "Roboto", Arial, sans-serif; font-weight: 700;
  }
  .contact__name { font-size: 22px; text-transform: uppercase; }
  .contact__phone { font-size: 56px; color: var(--green); line-height: 1.1; letter-spacing: 1px; }
  .contact__email { font-size: 22px; }
</style>
</head>
<body>

<section class="page page--front">
  <div class="front-hero" role="img" aria-label="Photo of a lead stand with hooks against a high-rise city view"></div>
  <svg class="front-accent" width="560" height="200" viewBox="0 0 560 200" aria-hidden="true">
    <polygon points="0,30 560,140 560,200 0,200" fill="var(--black)"/>
    <polygon points="0,20 60,32 60,120 0,120" fill="var(--green)"/>
    <polygon points="500,130 560,140 560,175 500,165" fill="var(--green)"/>
  </svg>
  <h1 class="product-title">Corvimax Stand</h1>
  <div class="photo-strip">
    <div class="photo photo--rooftop" role="img" aria-label="Stands holding leads on a rooftop with scaffold"></div>
    <div class="photo photo--city" role="img" aria-label="Stand on a balcony overlooking city towers"></div>
    <div class="photo photo--worker" role="img" aria-label="Worker in hi-vis beside a stand on scaffolding"></div>
  </div>
  <p class="intro">With Government legislation a requirement all electrical cords be elevated a minimum of 2 meters on construction sites - <strong>THE CORVIMAX STAND</strong> was developed. With over thirty years experience in the construction industry and safety requirements that continue to evolve we have designed and developed a lead stand that is ergonomic, portable and versatile. With no other product like it on the market.</p>
</section>

<section class="page page--back">
  <div class="back-top" role="img" aria-label="Faded city skyline background"></div>
  <svg class="back-accent" width="560" height="140" viewBox="0 0 560 140" aria-hidden="true">
    <polygon points="0,70 560,10 560,140 0,140" fill="var(--black)"/>
    <polygon points="500,16 560,10 560,40 500,46" fill="var(--green)"/>
  </svg>
  <div class="benefits">
    <h2 class="section-title">BENEFITS</h2>
    <ul class="bullets">
      <li>Unique portable and easy to assemble Corvistand to fit in most tool boxes</li>
      <li>Non-conductive and highly visible</li>
      <li>Indoor and outdoor use</li>
      <li>Leads the way in working safely</li>
      <li>Complies with Government legislation</li>
      <li>Construction sites, Outdoor events and Camping grounds</li>
    </ul>
  </div>
  <div class="product-card">
    <span class="product-card__name">Corvimax Stand</span>
    <div class="product-card__drawing" role="img" aria-label="Drawing of the telescopic stand with its wall spike"></div>
  </div>
  <div class="functions">
    <h2 class="section-title">FUNCTIONS</h2>
    <ul class="bullets">
      <li>Fully adjustable Telescopic Corvistand from 1.2 meters to 4.2 meters</li>
      <li>Spring loaded to lock between two surfaces</li>
      <li>Supports multiple leads, including temporary lighting and can also be used for Laser levels</li>
      <li>Can be screwed to a wall to elevate above floor finishes</li>
    </ul>
  </div>
  <div class="side-photos">
    <div class="photo photo--site-walk" role="img" aria-label="Worker walking past stands holding leads on a building site"></div>
    <div class="side-photos__lower">
      <div class="photo photo--floor" role="img" aria-label="Stand base set on a floor beside materials"></div>
      <div class="photo photo--wall" role="img" aria-label="Stand screwed to a wall with a laser level attached"></div>
    </div>
  </div>
  <div class="contact">
    <p class="contact__name">Marisa Thorne</p>
    <p class="contact__phone">049.173.6628</p>
    <p class="contact__email">brontavel@mailfern.example</p>
  </div>
</section>

</body>
</html>
```